I need two seperate flyers made
I have supplied 2 x photos of bathrooms, one for each flyer.
First flyer i want a banner or some sort of blockout acccross the bottom with my business name Marlow Bathrooms and my number 0487650923 and the promo is '' Renovate your bathroom from $10990 and in small writing under neath say owner to supply fixtures and tiles

Second flyer to have the same banner accross bottom and the promo is
Complete bathroom renovations from $15990 with small writing under saying terms and conditions apply

Want these to look professional and eye cathcing to generate more work.

I have attached 2x of our old flyers for reference and our current logo for use
Looking forward to working with you.

```html
<!DOCTYPE html>
<html lang="en">
<head>
<meta charset="utf-8">
<title>Marlow Bathrooms – Renovation Flyers</title>
<link href="https://fonts.googleapis.com/css2?family=Poppins:wght@400;600;700;800&display=swap" rel="stylesheet">
<style>
  :root {
    --brand-blue: #0a72c4;
    --ink: #1e1e1e;
    --bar: #262626;
    --paper: #ffffff;
    --backdrop: #ececec;
    --warm-light: #e4e1dc;
    --warm-mid: #c9c1b5;
    --warm-dark: #9e958a;
    --cool-light: #eceded;
    --cool-mid: #d2d4d5;
    --cool-dark: #a9acae;
  }
  * { margin: 0; padding: 0; box-sizing: border-box; }
  html, body {
    width: 782px; height: 1200px; overflow: hidden;
    background: var(--backdrop);
    font-family: "Poppins", sans-serif;
  }
  .canvas { position: relative; width: 782px; height: 1200px; }
  .flyer-slot {
    position: absolute; left: 175px;
    width: 432px; height: 558px;
    box-shadow: 0 5px 16px rgba(0,0,0,0.15);
  }
  .flyer-slot.first { top: 28px; }
  .flyer-slot.second { top: 614px; }
  .flyer {
    position: absolute; left: 0; top: 0;
    width: 600px; height: 775px;
    transform: scale(0.72); transform-origin: top left;
    background: var(--paper);
    overflow: hidden;
  }
  .hero-art { position: absolute; left: 0; top: 0; width: 600px; height: 655px; }
  .headline {
    position: absolute; left: 32px; top: 338px;
    font-weight: 800; font-size: 54px; line-height: 49px;
    letter-spacing: -0.5px; text-transform: uppercase; white-space: nowrap;
  }
  .headline .business { color: var(--ink); display: block; }
  .headline .credential { color: var(--brand-blue); display: block; }
  .offer { position: absolute; left: 33px; top: 548px; }
  .offer-lead { font-size: 16px; color: var(--ink); white-space: nowrap; }
  .offer-price {
    font-weight: 800; font-size: 72px; line-height: 70px;
    color: var(--brand-blue); letter-spacing: -1px;
  }
  .offer-note {
    position: absolute; top: 553px;
    font-size: 15px; line-height: 24.5px; color: var(--ink);
  }
  .first .offer-note { left: 306px; }
  .second .offer-note { left: 368px; }
  .contact-bar {
    position: absolute; left: 0; top: 655px;
    width: 600px; height: 120px; background: var(--bar);
  }
  .brand-name {
    position: absolute; left: 33px; top: 38px;
    display: flex; align-items: center; gap: 10px;
    color: var(--paper); font-weight: 600; font-size: 17px;
    line-height: 21px; text-transform: uppercase; letter-spacing: 2px;
  }
  .brand-mark { width: 14px; height: 14px; background: var(--paper); }
  .contact-line {
    position: absolute; left: 305px;
    display: flex; align-items: center; gap: 11px; color: var(--paper);
    white-space: nowrap;
  }
  .contact-phone { top: 14px; height: 36px; font-weight: 700; font-size: 33px; letter-spacing: 0.3px; }
  .contact-web { top: 54px; height: 36px; font-weight: 700; font-size: 13px; }
  .contact-icon { width: 36px; height: 36px; flex: none; }
</style>
</head>
<body>
<main class="canvas">

  <section class="flyer-slot first">
    <article class="flyer">
      <svg class="hero-art" viewBox="0 0 600 655">
        <defs>
          <linearGradient id="warm-tones" x1="0" y1="0" x2="1" y2="1">
            <stop offset="0" stop-color="var(--warm-light)"/>
            <stop offset="0.6" stop-color="var(--warm-mid)"/>
            <stop offset="1" stop-color="var(--warm-dark)"/>
          </linearGradient>
        </defs>
        <polygon role="img" aria-label="Photo of a renovated bathroom with floating vanity, oval mirror and terrazzo walk-in shower"
                 points="0,0 600,0 600,482 0,154" fill="url(#warm-tones)"/>
        <polygon class="accent-band" points="0,154 600,482 600,502 0,174" fill="var(--brand-blue)"/>
        <polygon class="accent-triangle" points="0,184 168,274 0,347" fill="var(--brand-blue)"/>
      </svg>

      <h1 class="headline">
        <span class="business">Marlow</span>
        <span class="business">Bathrooms</span>
        <span class="credential">Fully Licensed</span>
        <span class="credential">&amp; Insured</span>
      </h1>

      <div class="offer">
        <p class="offer-lead">Renovate your bathroom from</p>
        <p class="offer-price">$10990</p>
      </div>
      <p class="offer-note">and in small writing under<br>neath say owner to supply<br>fixtures and tiles</p>

      <footer class="contact-bar">
        <div class="brand-name">
          <span class="brand-mark"></span>
          <span>Marlow<br>Bathrooms</span>
        </div>
        <div class="contact-line contact-phone">
          <svg class="contact-icon" viewBox="0 0 36 36" aria-hidden="true">
            <circle cx="18" cy="18" r="17" fill="var(--brand-blue)" stroke="#fff" stroke-width="2"/>
            <path d="M12 10c1-1 2-1 3 0l2 3c.5 1 .3 2-.5 2.6l-1 .8c.8 2 2.3 3.6 4.3 4.5l.8-1c.6-.8 1.6-1 2.6-.5l3 2c1 .7 1 2 0 3l-1.5 1.5c-1.5 1.3-4 1-7-1-3.2-2.2-5.6-5-6.8-8-1-2.6-.8-4.5.6-5.900z" fill="#fff"/>
          </svg>
          <span>0487650923</span>
        </div>
        <div class="contact-line contact-web">
          <svg class="contact-icon" viewBox="0 0 36 36" aria-hidden="true">
            <circle cx="18" cy="18" r="17" fill="var(--brand-blue)" stroke="#fff" stroke-width="2"/>
            <g fill="none" stroke="#fff" stroke-width="1.6">
              <circle cx="18" cy="18" r="9"/>
              <ellipse cx="18" cy="18" rx="4" ry="9"/>
              <line x1="9" y1="18" x2="27" y2="18"/>
              <line x1="10.5" y1="13.5" x2="25.5" y2="13.5"/>
              <line x1="10.5" y1="22.5" x2="25.5" y2="22.5"/>
            </g>
          </svg>
          <span>www.Marlowbathrooms.com.au</span>
        </div>
      </footer>
    </article>
  </section>

  <section class="flyer-slot second">
    <article class="flyer">
      <svg class="hero-art" viewBox="0 0 600 655">
        <defs>
          <linearGradient id="cool-tones" x1="0" y1="0" x2="1" y2="1">
            <stop offset="0" stop-color="var(--cool-light)"/>
            <stop offset="0.6" stop-color="var(--cool-mid)"/>
            <stop offset="1" stop-color="var(--cool-dark)"/>
          </linearGradient>
        </defs>
        <polygon role="img" aria-label="Photo of a white renovated bathroom with backlit round mirror, vanity, freestanding bath and pendant light"
                 points="0,0 600,0 600,482 0,154" fill="url(#cool-tones)"/>
        <polygon class="accent-band" points="0,154 600,482 600,502 0,174" fill="var(--brand-blue)"/>
        <polygon class="accent-triangle" points="0,184 168,274 0,347" fill="var(--brand-blue)"/>
      </svg>

      <h1 class="headline">
        <span class="business">Marlow</span>
        <span class="business">Bathrooms</span>
        <span class="credential">Fully Licensed</span>
        <span class="credential">&amp; Insured</span>
      </h1>

      <div class="offer">
        <p class="offer-lead">Complete bathroom renovations from</p>
        <p class="offer-price">$15990</p>
      </div>
      <p class="offer-note">with small writing under<br>saying terms and<br>conditions apply</p>

      <footer class="contact-bar">
        <div class="brand-name">
          <span class="brand-mark"></span>
          <span>Marlow<br>Bathrooms</span>
        </div>
        <div class="contact-line contact-phone">
          <svg class="contact-icon" viewBox="0 0 36 36" aria-hidden="true">
            <circle cx="18" cy="18" r="17" fill="var(--brand-blue)" stroke="#fff" stroke-width="2"/>
            <path d="M12 10c1-1 2-1 3 0l2 3c.5 1 .3 2-.5 2.6l-1 .8c.8 2 2.3 3.6 4.3 4.5l.8-1c.6-.8 1.6-1 2.6-.5l3 2c1 .7 1 2 0 3l-1.5 1.5c-1.5 1.3-4 1-7-1-3.2-2.2-5.6-5-6.8-8-1-2.6-.8-4.5.6-5.900z" fill="#fff"/>
          </svg>
          <span>0487650923</span>
        </div>
        <div class="contact-line contact-web">
          <svg class="contact-icon" viewBox="0 0 36 36" aria-hidden="true">
            <circle cx="18" cy="18" r="17" fill="var(--brand-blue)" stroke="#fff" stroke-width="2"/>
            <g fill="none" stroke="#fff" stroke-width="1.6">
              <circle cx="18" cy="18" r="9"/>
              <ellipse cx="18" cy="18" rx="4" ry="9"/>
              <line x1="9" y1="18" x2="27" y2="18"/>
              <line x1="10.5" y1="13.5" x2="25.5" y2="13.5"/>
              <line x1="10.5" y1="22.5" x2="25.5" y2="22.5"/>
            </g>
          </svg>
          <span>www.Marlowbathrooms.com.au</span>
        </div>
      </footer>
    </article>
  </section>

</main>
</body>
</html>
```